Cover-Design für Office Notizbuch gesucht
Zielgruppe
Wir erstellen schöne Officeprodukte für junge, modebewusste (und alte) Mädels. Es soll also sehr quillorat / moranteve tauglich sein.
Aufgabenstellung
Wir möchten ein Din A5 Notizbuch haben und suchen dafür ein tolles Coverdesign.
Es soll ein zeitloses Design haben, gerne mit einem motivierenden Spruch oder einfach einem schönen Muster und Design.
Zusätzlich kann auch mit einer Heißfolienprägung Gold gearbeitet werden.

```html
<!DOCTYPE html>
<html lang="en">
<head>
<meta charset="utf-8">
<title>Notebook Covers – Positive Vibes</title>
<link rel="stylesheet" href="https://fonts.googleapis.com/css2?family=Caveat+Brush&family=Caveat:wght@500&display=swap">
<style>
  :root {
    --page-bg: #ffffff;
    --teal: #5e9f9a;
    --teal-deep: #4f8c88;
    --sand: #e6d7b8;
    --rose: #d95a6e;
    --cream: #ecebe3;
    --charcoal: #2b2b2a;
    --ink: #1f1d1c;
    --gold: #c9a04a;
    --gold-light: #e2c27a;
    --lettering-light: #dccdb0;
  }
  * { margin: 0; padding: 0; box-sizing: border-box; }
  html, body {
    width: 1200px;
    height: 848px;
    overflow: hidden;
    background: var(--page-bg);
  }
  .canvas {
    position: relative;
    width: 1200px;
    height: 848px;
  }
  .cover {
    position: absolute;
    top: 102px;
    width: 448px;
    height: 611px;
    border-radius: 4px;
    overflow: hidden;
  }
  .cover--light { left: 92px; }
  .cover--dark { left: 650px; }
  .cover__pattern {
    position: absolute;
    inset: 0;
    width: 100%;
    height: 100%;
  }
  .badge {
    position: absolute;
    left: 52px;
    top: 128px;
    width: 340px;
    height: 340px;
    border-radius: 50%;
    display: flex;
    flex-direction: column;
    align-items: center;
    justify-content: center;
    text-align: center;
  }
  .cover--light .badge { background: var(--cream); color: var(--ink); }
  .cover--dark .badge { background: var(--charcoal); color: var(--lettering-light); }
  .badge__rings {
    position: absolute;
    inset: 0;
    width: 100%;
    height: 100%;
  }
  .badge__line {
    position: relative;
    font-family: "Caveat", cursive;
    font-weight: 500;
    font-size: 34px;
    line-height: 1;
  }
  .badge__line--top { transform: translateX(-10px); }
  .badge__line--bottom { transform: translateX(14px); }
  .badge__headline {
    position: relative;
    font-family: "Caveat Brush", cursive;
    font-size: 84px;
    line-height: 0.8;
    margin: 6px 0 8px;
  }
</style>
</head>
<body>
<main class="canvas">

  <section class="cover cover--light">
    <svg class="cover__pattern" role="img" aria-label="Floral pattern of stylised teal, sand and rose flowers" viewBox="0 0 448 611" preserveAspectRatio="none">
      <defs>
        <radialGradient id="floral-light" cx="0.75" cy="0.72" r="0.8">
          <stop offset="0" stop-color="var(--rose)" stop-opacity="0.55"/>
          <stop offset="0.25" stop-color="var(--sand)" stop-opacity="0.45"/>
          <stop offset="0.6" stop-color="var(--teal)"/>
          <stop offset="1" stop-color="var(--teal-deep)"/>
        </radialGradient>
      </defs>
      <rect width="448" height="611" fill="var(--teal)"/>
      <rect width="448" height="611" fill="url(#floral-light)"/>
    </svg>
    <div class="badge">
      <svg class="badge__rings" viewBox="0 0 340 340" aria-hidden="true">
        <circle cx="170" cy="170" r="150" fill="none" stroke="var(--gold)" stroke-width="2"/>
        <circle cx="172" cy="168" r="144" fill="none" stroke="var(--gold-light)" stroke-width="1.5"/>
        <circle cx="168" cy="173" r="139" fill="none" stroke="var(--gold)" stroke-width="1"/>
      </svg>
      <p class="badge__line badge__line--top">positive mind</p>
      <h2 class="badge__headline">positive<br>vibes</h2>
      <p class="badge__line badge__line--bottom">positive life</p>
    </div>
  </section>

  <section class="cover cover--dark">
    <svg class="cover__pattern" role="img" aria-label="Floral pattern of stylised teal, sand and rose flowers" viewBox="0 0 448 611" preserveAspectRatio="none">
      <defs>
        <radialGradient id="floral-dark" cx="0.75" cy="0.72" r="0.8">
          <stop offset="0" stop-color="var(--rose)" stop-opacity="0.55"/>
          <stop offset="0.25" stop-color="var(--sand)" stop-opacity="0.45"/>
          <stop offset="0.6" stop-color="var(--teal)"/>
          <stop offset="1" stop-color="var(--teal-deep)"/>
        </radialGradient>
      </defs>
      <rect width="448" height="611" fill="var(--teal)"/>
      <rect width="448" height="611" fill="url(#floral-dark)"/>
    </svg>
    <div class="badge">
      <svg class="badge__rings" viewBox="0 0 340 340" aria-hidden="true">
        <circle cx="170" cy="170" r="150" fill="none" stroke="var(--gold)" stroke-width="2"/>
        <circle cx="172" cy="168" r="144" fill="none" stroke="var(--gold-light)" stroke-width="1.5"/>
        <circle cx="168" cy="173" r="139" fill="none" stroke="var(--gold)" stroke-width="1"/>
      </svg>
      <p class="badge__line badge__line--top">positive mind</p>
      <h2 class="badge__headline">positive<br>vibes</h2>
      <p class="badge__line badge__line--bottom">positive life</p>
    </div>
  </section>

</main>
</body>
</html>
```